Web Design for Independent Pet Supply shop.

Larchmont Critter Depot is a locally owned and operated premium natural pet food store and supply company with 2 thriving retail stores in Bend, Oregon, and a home delivery service. The pet food offered is the best on the market and may be described as “holistic”. Also on offer is a vast selection of toys, training tools, treats, and other supplies, as well as dog washing services that range from "do-it yourself" to "spa." Current site: LarchmontCritterDepot.com. They need a new, updated and responsive site.
Likes:
Vondals.com: Natural colors, not loud, pages in motion, simple & clean but very informative.
Tobiasmerrow.com: Everything in simple big colorful blocks. The specials run across the top and in motion. This site looks very professional but simple. The information is available several different places.
Greenbarrel.com: Again big blocks through out. Very Fun and inviting. Tons of information with videos and recipes and testimonials. Pleasant feel and colors as well.
Dislikes:
Furvana.com: Looks cheap, hate the colors, very busy and over whelming. Hate the old style header bar going across with options. Too many printed words instead of fun images.
Colors should be "natural" tones, warm and soothing. Deep dark blue and greys with earthy wood color.
Do Not Use: Blue violet, violet, red violet

```html
<!DOCTYPE html>
<html lang="en">
<head>
<meta charset="utf-8">
<title>Larchmont Critter Depot</title>
<link href="https://fonts.googleapis.com/css2?family=Oswald:wght@300;400&family=PT+Sans+Narrow:wght@400;700&family=Source+Sans+3:ital,wght@0,400;0,600;1,400;1,600&display=swap" rel="stylesheet">
<style>
:root{
  --charcoal:#3b3b3b;
  --news-bg:#404040;
  --wood:#b8864a;
  --wood-dark:#9c6f36;
  --paper:#f8f8f8;
  --paper-grey:#eeeeee;
  --ink:#3a3a3a;
  --muted:#cfcfcf;
  --white:#ffffff;
  --heading:"PT Sans Narrow", sans-serif;
  --body:"Source Sans 3", sans-serif;
  --display:"Oswald", sans-serif;
}
*{box-sizing:border-box;margin:0;padding:0}
html,body{width:1200px;height:2200px;overflow:hidden}
body{font-family:var(--body);color:var(--ink);background:var(--paper);position:relative}
a{color:inherit;text-decoration:none}

/* header */
.site-header{position:absolute;top:0;left:0;width:1200px;height:63px;background:var(--charcoal);border-bottom:3px solid var(--wood);z-index:2}
.brand{position:absolute;left:208px;top:0;height:60px;display:flex;align-items:center;gap:6px;white-space:nowrap}
.brand-dot{width:16px;height:16px;border-radius:50%;background:var(--wood);flex:none}
.brand-name{font-family:var(--heading);font-weight:700;font-size:15px;color:var(--wood);text-transform:uppercase}
.main-nav{position:absolute;left:411px;top:0;height:60px;display:flex}
.main-nav a{height:60px;line-height:60px;padding:0 11px;color:var(--white);font-size:14px;white-space:nowrap}
.main-nav a.is-current{background:var(--wood);padding:0 24px}

/* hero */
.hero{position:absolute;top:63px;left:0;width:1200px;height:445px;text-align:center;color:var(--white)}
.hero-photo{position:absolute;inset:0;background:radial-gradient(ellipse at 52% 45%,#c27a3a 0%,#a8652f 25%,#8d7663 48%,#b9bcbd 75%,#d5d8d9 100%)}
.hero-photo::after{content:"";position:absolute;inset:0;background:rgba(0,0,0,.12)}
.hero-content{position:absolute;left:0;right:0;top:165px}
.hero-title{font-family:var(--display);font-weight:300;font-size:42px;text-transform:uppercase;text-shadow:0 1px 3px rgba(0,0,0,.4);white-space:nowrap}
.hero-text{width:560px;margin:8px auto 0;font-size:12px;line-height:15px;text-shadow:0 1px 2px rgba(0,0,0,.5)}
.hero-button{display:inline-block;margin-top:26px;width:123px;height:38px;line-height:38px;background:var(--charcoal);border-radius:3px;font-size:13.5px;text-transform:uppercase}
.hero-arrow{position:absolute;top:196px}
.hero-arrow.prev{left:213px}
.hero-arrow.next{left:981px}
.hero-dots{position:absolute;top:409px;left:605px;display:flex;gap:12px}
.hero-dots span{width:13px;height:13px;border-radius:50%;background:var(--charcoal)}

/* features */
.features{position:absolute;top:508px;left:0;width:1200px;height:255px;background:var(--paper);display:flex;justify-content:center}
.feature{width:286px;text-align:center;padding-top:53px}
.feature-icon{width:80px;height:80px;margin:0 auto}
.feature-text{margin-top:19px;font-size:14.5px;line-height:18px;color:var(--ink)}
.feature-link{display:inline-block;margin-top:14px;font-size:11px;font-style:italic;font-weight:600;color:var(--wood);text-decoration:underline}

/* products */
.products{position:absolute;top:763px;left:0;width:1200px;height:406px;background:var(--paper-grey)}
.section-title{font-family:var(--heading);font-weight:700;font-size:25px;text-transform:uppercase;color:var(--ink)}
.products .section-title{position:absolute;left:207px;top:40px}
.carousel-arrows{position:absolute;left:985px;top:44px;font-family:var(--heading);font-weight:700;font-size:22px;color:var(--ink);letter-spacing:4px}
.product-list{position:absolute;left:207px;top:96px;display:flex;gap:16px}
.product-card{width:190px;height:238px;background:var(--white);border:1px solid #d8d8d8}
.product-photo{height:186px}
.product-photo.food{background:linear-gradient(90deg,#3a3a3a 0 58%,#b22b24 58% 100%)}
.product-photo.care{background:linear-gradient(90deg,#ffffff 0 55%,#e9e1d2 55% 100%)}
.product-name{height:51px;line-height:51px;text-align:center;font-family:var(--heading);font-weight:700;font-size:17px;text-transform:uppercase;color:var(--white);background:var(--charcoal)}
.product-card.is-active .product-name{background:var(--wood)}

/* news */
.news{position:absolute;top:1169px;left:0;width:1200px;height:433px;background:var(--news-bg);color:var(--white)}
.news .section-title{position:absolute;left:207px;top:40px;color:var(--white)}
.news-item{position:absolute;width:400px;display:flex;gap:23px}
.news-photo{width:110px;height:110px;flex:none;border:1px solid #555;background:linear-gradient(135deg,#6e5a4e,#2f3b55)}
.news-title{font-family:var(--heading);font-weight:700;font-size:19px;margin-top:-3px}
.news-meta{font-size:11px;font-style:italic;font-weight:600;color:var(--muted)}
.news-text{margin-top:10px;font-size:10.5px;line-height:13px;color:var(--muted);width:250px}
.read-more{display:inline-block;margin-top:8px;height:25px;line-height:25px;padding:0 12px;border-radius:3px;background:var(--wood);color:var(--white);font-size:11.5px}
.read-more.is-light{background:var(--white);color:var(--ink)}

/* promo blocks */
.promos{position:absolute;top:1602px;left:0;width:1200px;height:285px;background:var(--paper)}
.promo{position:absolute;top:52px;width:378px;height:186px;display:flex}
.promo-photo{width:200px;height:186px;background:radial-gradient(ellipse at 45% 45%,#e0b57a 0%,#c07a3a 40%,#5b2a14 100%)}
.promo-body{flex:1;background:var(--wood);padding:30px 14px 0 26px;color:var(--white)}
.promo-title{font-family:var(--heading);font-weight:700;font-size:28px;text-transform:uppercase;color:#f3e3c8;line-height:28px}
.promo-text{margin-top:6px;font-size:10px;line-height:12px;color:#f6ead8;width:110px}
.promo .read-more{background:var(--charcoal);margin-top:12px;height:24px;line-height:24px}

/* footer */
.site-footer{position:absolute;top:1887px;left:0;width:1200px;height:313px;background:var(--charcoal);color:var(--white)}
.footer-brand{position:absolute;left:213px;top:50px;height:30px;display:flex;align-items:center;gap:6px;white-space:nowrap}
.footer-brand .brand-name{font-size:17px}
.footer-about{position:absolute;left:216px;top:118px;width:200px;font-size:12.5px;line-height:16px}
.footer-about p+p{margin-top:16px}
.footer-col{position:absolute;top:83px}
.footer-col h3{font-family:var(--heading);font-weight:700;font-size:16px;text-transform:uppercase;margin-bottom:16px}
.footer-col li{list-style:none;font-size:12px;line-height:19.5px}
.col-company{left:487px}
.col-follow{left:646px}
.col-follow li{line-height:21.5px}
.col-contact{left:797px;top:80px}
.contact-row{display:flex;font-size:12px;line-height:21px}
.contact-row dt{width:70px}
</style>
</head>
<body>

<header class="site-header">
  <a class="brand" href="#"><span class="brand-dot"></span><span class="brand-name">Larchmont Critter Depot</span></a>
  <nav class="main-nav">
    <a class="is-current" href="#">Home</a>
    <a href="#">Events</a>
    <a href="#">Blog</a>
    <a href="#">About</a>
    <a href="#">Dog Wash</a>
    <a href="#">Resources</a>
    <a href="#">Products</a>
    <a href="#">Links</a>
    <a href="#">Contact</a>
  </nav>
</header>

<section class="hero">
  <div class="hero-photo" role="img" aria-label="Golden retriever resting outdoors, looking up to the right"></div>
  <svg class="hero-arrow prev" width="20" height="36" viewBox="0 0 20 36"><path d="M17 2 L4 18 L17 34" fill="none" stroke="#b8864a" stroke-width="5"/></svg>
  <svg class="hero-arrow next" width="20" height="36" viewBox="0 0 20 36"><path d="M3 2 L16 18 L3 34" fill="none" stroke="#b8864a" stroke-width="5"/></svg>
  <div class="hero-content">
    <h1 class="hero-title">Welcome to Larchmont Critter Depot</h1>
    <p class="hero-text">Lorem ipsum dolor sit amet, consectetur adipisicing elit, sed do eiusmod tempor incididunt ut labore et dolore magna aliqua. Ut enim ad minim veniam, quis nostrud exercitation ullamco laboris nisi ut aliquip ex ea commodo consequat. Duis aute irure dolor in reprehenderit in voluptate velit esse cillum</p>
    <a class="hero-button" href="#">Read More</a>
  </div>
  <div class="hero-dots"><span></span><span></span></div>
</section>

<section class="features">
  <div class="feature">
    <svg class="feature-icon" viewBox="0 0 80 80"><circle cx="40" cy="40" r="39" fill="#b8864a"/><path d="M20 41 L40 22 L60 41 L55 41 L55 58 L46 58 L46 46 L34 46 L34 58 L25 58 L25 41 Z" fill="#fff"/></svg>
    <p class="feature-text">Lorem ipsum dolor sit amet,<br>consectetur dipisicing elit, sed do</p>
    <a class="feature-link" href="#">Continue reading...</a>
  </div>
  <div class="feature">
    <svg class="feature-icon" viewBox="0 0 80 80"><circle cx="40" cy="40" r="39" fill="#b8864a"/><path d="M33 44 L28 62 L35 58 L38 64 L40 48 Z M47 44 L52 62 L45 58 L42 64 L40 48 Z" fill="#fff"/><circle cx="40" cy="34" r="14" fill="#fff"/><circle cx="40" cy="34" r="9" fill="none" stroke="#b8864a" stroke-width="2"/><rect x="39" y="29" width="2" height="7" fill="#b8864a"/><circle cx="40" cy="39" r="1.3" fill="#b8864a"/></svg>
    <p class="feature-text">Lorem ipsum dolor sit amet,<br>consectetur dipisicing elit, sed do</p>
    <a class="feature-link" href="#">Continue reading...</a>
  </div>
  <div class="feature">
    <svg class="feature-icon" viewBox="0 0 80 80"><circle cx="40" cy="40" r="39" fill="#b8864a"/><rect x="34" y="23" width="12" height="7" rx="2" fill="none" stroke="#fff" stroke-width="3"/><rect x="21" y="29" width="38" height="28" rx="4" fill="#fff"/><path d="M37 36 h6 v5 h5 v6 h-5 v5 h-6 v-5 h-5 v-6 h5 z" fill="#b8864a"/></svg>
    <p class="feature-text">Lorem ipsum dolor sit amet,<br>consectetur dipisicing elit, sed do</p>
    <a class="feature-link" href="#">Continue reading...</a>
  </div>
</section>

<section class="products">
  <h2 class="section-title">Our Products</h2>
  <div class="carousel-arrows">&#10094;&#10095;</div>
  <div class="product-list">
    <article class="product-card is-active">
      <div class="product-photo food" role="img" aria-label="Bowl of dry dog food beside a bag of kibble and a bulldog"></div>
      <div class="product-name">Product Name</div>
    </article>
    <article class="product-card">
      <div class="product-photo care" role="img" aria-label="Boxes of pet worming tablets beside a golden retriever"></div>
      <div class="product-name">Product Name</div>
    </article>
    <article class="product-card">
      <div class="product-photo food" role="img" aria-label="Bowl of dry dog food beside a bag of kibble and a bulldog"></div>
      <div class="product-name">Product Name</div>
    </article>
    <article class="product-card">
      <div class="product-photo care" role="img" aria-label="Boxes of pet worming tablets beside a golden retriever"></div>
      <div class="product-name">Product Name</div>
    </article>
  </div>
</section>

<section class="news">
  <h2 class="section-title">News &amp; Events</h2>
  <article class="news-item" style="left:208px;top:103px">
    <div class="news-photo" role="img" aria-label="Portrait of a smiling man in a suit"></div>
    <div><h3 class="news-title">Take a closer look.</h3><p class="news-meta">Aug 17, 2012 • 4</p><p class="news-text">Proin gravida nibh vel velit auctor aliquet. Aenean sollicitudin, lorem quis bibendum auctor, nisi elit</p><a class="read-more is-light" href="#">Read More</a></div>
  </article>
  <article class="news-item" style="left:660px;top:103px">
    <div class="news-photo" role="img" aria-label="Portrait of a smiling man in a suit"></div>
    <div><h3 class="news-title">Take a closer look.</h3><p class="news-meta">Aug 17, 2012 • 4</p><p class="news-text">Proin gravida nibh vel velit auctor aliquet. Aenean sollicitudin, lorem quis bibendum auctor, nisi elit</p><a class="read-more" href="#">Read More</a></div>
  </article>
  <article class="news-item" style="left:208px;top:263px">
    <div class="news-photo" role="img" aria-label="Portrait of a smiling man in a suit"></div>
    <div><h3 class="news-title">Take a closer look.</h3><p class="news-meta">Aug 17, 2012 • 4</p><p class="news-text">Proin gravida nibh vel velit auctor aliquet. Aenean sollicitudin, lorem quis bibendum auctor, nisi elit</p><a class="read-more" href="#">Read More</a></div>
  </article>
  <article class="news-item" style="left:660px;top:263px">
    <div class="news-photo" role="img" aria-label="Portrait of a smiling man in a suit"></div>
    <div><h3 class="news-title">Take a closer look.</h3><p class="news-meta">Aug 17, 2012 • 4</p><p class="news-text">Proin gravida nibh vel velit auctor aliquet. Aenean sollicitudin, lorem quis bibendum auctor, nisi elit</p><a class="read-more" href="#">Read More</a></div>
  </article>
</section>

<section class="promos">
  <article class="promo" style="left:207px">
    <div class="promo-photo" role="img" aria-label="Golden puppy holding a red rose"></div>
    <div class="promo-body"><h3 class="promo-title">Our Tips</h3><p class="promo-text">Proin gravida nibh vel velit auctor aliquet. Aenean sollicitudin, lorem quis bibendum auctor, nisi elit</p><a class="read-more" href="#">Read More</a></div>
  </article>
  <article class="promo" style="left:632px">
    <div class="promo-photo" role="img" aria-label="Golden puppy holding a red rose"></div>
    <div class="promo-body"><h3 class="promo-title">Breeds</h3><p class="promo-text">Proin gravida nibh vel velit auctor aliquet. Aenean sollicitudin, lorem quis bibendum auctor, nisi elit</p><a class="read-more" href="#">Read More</a></div>
  </article>
</section>

<footer class="site-footer">
  <div class="footer-brand"><span class="brand-dot"></span><span class="brand-name">Larchmont Critter Depot</span></div>
  <div class="footer-about">
    <p>Your about us information would fit here nicely.</p>
    <p>You could also just have an overview and use the link below to link to you full about us page.</p>
  </div>
  <div class="footer-col col-company">
    <h3>Company</h3>
    <ul><li>Home</li><li>Events</li><li>Blog</li><li>About</li><li>Dog Wash</li><li>Resources</li><li>Products</li><li>Link</li><li>Contact</li></ul>
  </div>
  <div class="footer-col col-follow">
    <h3>Follow Us</h3>
    <ul><li>Circlehub</li><li>Peeper</li><li>Pawbook</li><li>Worknet</li><li>RSS</li></ul>
  </div>
  <div class="footer-col col-contact">
    <h3>Contact Us</h3>
    <dl>
      <div class="contact-row"><dt>Telephone</dt><dd>+1400 555 010</dd></div>
      <div class="contact-row"><dt>FAX</dt><dd>+1504 555 0137</dd></div>
      <div class="contact-row"><dt>E-mail</dt><dd>larchmontcritterdepot.com</dd></div>
    </dl>
  </div>
</footer>

</body>
</html>
```